Belle Rive Weddings and Events

I am a small boutique wedding coordinator, stylist and bridal consultant/coach/assistant. I am based in Brisbane, Australia and my business is geared towards mid range- high end budget bridal couples.
I am after some business cards that are double sided, with the logo on one side and all other information on the other side, including the business tagline of design, create, celebrate. The look of the card needs to be clean and crisp, with white and the tones of grey of the logo.The final design needs to convey sophistication and poise. Perhaps the logo and tagline could be done in a metallic silver with the rest of the text in the shades of grey from the style guide attached below.
Title- Mira Tolvarenko - Director / Events Manager and Stylist
Address - 218 Halbrook Terrace, Wexley Vale, QLD, 4127
Phone- 07 3894 2167
Mobile- 0438 725 519
Email- Mira@bellerivecelebra.com.au
Website- www.bellerivecelebra.com.au

```html
<!DOCTYPE html>
<html lang="en">
<head>
<meta charset="utf-8">
<title>Belle Rive Weddings and Events – Business Card</title>
<link href="https://fonts.googleapis.com/css2?family=Questrial&display=swap" rel="stylesheet">
<style>
  :root {
    --backdrop: #e9e9ea;
    --card: #ffffff;
    --ink-strong: #7a7a7c;
    --ink-soft: #8f8f91;
    --silver: #b4b4b8;
    --silver-soft: #e4e4e6;
    --shadow: rgba(0, 0, 0, 0.10);
  }
  * { box-sizing: border-box; margin: 0; padding: 0; }
  html, body {
    width: 1200px;
    height: 1192px;
    overflow: hidden;
    background: var(--backdrop);
    font-family: "Questrial", "Century Gothic", sans-serif;
  }
  .sheet {
    position: relative;
    width: 1200px;
    height: 1192px;
  }
  .card {
    position: absolute;
    left: 250px;
    width: 700px;
    height: 400px;
    background: var(--card);
    box-shadow: 0 10px 30px var(--shadow);
  }
  .card--front { top: 150px; }
  .card--back { top: 642px; }

  /* Front: brand name and tagline */
  .brand {
    position: absolute;
    top: 50%;
    left: 50%;
    transform: translate(-50%, -50%);
    display: flex;
    flex-direction: column;
    align-items: center;
    gap: 14px;
    color: var(--silver);
  }
  .brand__row {
    display: flex;
    align-items: center;
    gap: 16px;
  }
  .brand__dot {
    width: 12px;
    height: 12px;
    border-radius: 50%;
    background: var(--silver);
  }
  .brand__name {
    font-size: 30px;
    letter-spacing: 1px;
    line-height: 1.25;
    text-align: center;
  }
  .brand__rule {
    width: 120px;
    height: 1px;
    background: var(--silver-soft);
  }
  .brand__tagline {
    font-size: 13px;
    letter-spacing: 4px;
    text-transform: lowercase;
    color: var(--silver);
  }

  /* Back: contact details */
  .details {
    position: absolute;
    left: 92px;
    top: 50%;
    transform: translateY(-50%);
    width: 530px;
  }
  .ornament {
    width: 200px;
    height: 48px;
    background: radial-gradient(ellipse at center, var(--silver-soft) 0%, rgba(228, 228, 230, 0.5) 45%, rgba(255, 255, 255, 0) 72%);
  }
  .ornament--top { margin: 0 0 14px 160px; }
  .ornament--bottom { margin: 14px 0 0 0; }
  .person {
    font-size: 19px;
    color: var(--ink-strong);
    margin-bottom: 12px;
    white-space: nowrap;
  }
  .person__name { font-weight: 700; }
  .contact {
    list-style: none;
    font-size: 14px;
    line-height: 1.6;
    color: var(--ink-soft);
  }
  .contact__label {
    font-weight: 700;
    color: var(--ink-strong);
    margin-right: 4px;
  }
</style>
</head>
<body>
<main class="sheet">
  <section class="card card--front" aria-label="Card front">
    <div class="brand">
      <div class="brand__row">
        <span class="brand__dot"></span>
        <span class="brand__name">Belle Rive<br>Weddings and Events</span>
      </div>
      <span class="brand__rule"></span>
      <span class="brand__tagline">design, create, celebrate</span>
    </div>
  </section>

  <section class="card card--back" aria-label="Card back">
    <div class="details">
      <div class="ornament ornament--top" role="img" aria-label="Silver scrollwork flourish divider"></div>
      <p class="person"><span class="person__name">Mira Tolvarenko</span> - Director / Events Manager and Stylist</p>
      <ul class="contact">
        <li><span class="contact__label">Address</span>218 Halbrook Terrace, Wexley Vale, QLD, 4127</li>
        <li><span class="contact__label">Phone</span>07 3894 2167 <span class="contact__label">Mobile</span>0438 725 519</li>
        <li><span class="contact__label">Email</span>Mira@bellerivecelebra.com.au</li>
        <li><span class="contact__label">Website</span>www.bellerivecelebra.com.au</li>
      </ul>
      <div class="ornament ornament--bottom" role="img" aria-label="Silver scrollwork flourish divider"></div>
    </div>
  </section>
</main>
</body>
</html>
```